Business Card Design Project

Hi

I have a draft of a business card which I need smarting up. I have attached the pdf of this.
The information on the front is correct.
The information on the back should contain:
Project Management, Consulting, Master Systems Integrator, Datacenter, Relocations, Restacks. I want this spiraling around the back

Can you change the telephone number to +65 8476 2153.

Target Market(s)

Chief Technology Officers of large multi-nationals

Industry/Entity Type

Business

Requirements
Must have
• My logo - Vorbelt (attached)
The orange and blue colour running around the edge

```html
<!DOCTYPE html>
<html lang="en">
<head>
<meta charset="utf-8">
<title>Vorbelt Business Card</title>
<link rel="stylesheet" href="https://fonts.googleapis.com/css2?family=Exo+2:wght@300;700&family=Open+Sans:wght@400&display=swap">
<style>
  :root {
    --canvas: #d9d9d9;
    --card-dark: #0d0d0d;
    --card-mid: #1c1c1c;
    --card-edge: #262626;
    --wordmark: #8a8a8a;
    --text-light: #c9c9c9;
    --text-white: #ffffff;
    --accent-orange: #f39117;
    --accent-cyan: #2fd2e0;
    --tile: #2a2626;
  }
  * { margin: 0; padding: 0; box-sizing: border-box; }
  html, body { width: 1200px; height: 861px; overflow: hidden; }
  body {
    background: radial-gradient(ellipse at 50% 40%, #ececec 0%, var(--canvas) 75%);
    font-family: "Open Sans", Arial, sans-serif;
    position: relative;
  }
  .card {
    position: absolute;
    top: 268px;
    width: 540px;
    height: 324px;
    border-radius: 4px;
    overflow: hidden;
    background: linear-gradient(135deg, var(--card-mid) 0%, var(--card-dark) 60%, #050505 100%);
    box-shadow: 0 10px 30px rgba(0,0,0,0.35);
  }
  .card--back { left: 40px; }
  .card--front { left: 620px; }

  /* Back side */
  .brand-lockup {
    position: absolute;
    left: 46px;
    top: 62px;
    display: flex;
    align-items: center;
    gap: 22px;
  }
  .brand-tile {
    width: 104px;
    height: 104px;
    border-radius: 18px;
    background: var(--tile);
  }
  .brand-name {
    font-family: "Exo 2", Arial, sans-serif;
    font-weight: 300;
    font-size: 62px;
    color: var(--wordmark);
    letter-spacing: 1px;
  }
  .service-list {
    position: absolute;
    list-style: none;
    font-size: 13px;
    color: var(--text-light);
    line-height: 19px;
  }
  .service-list--main { left: 150px; top: 198px; }
  .service-list--extra { left: 370px; top: 190px; }
  .service-list li { display: flex; align-items: center; gap: 8px; }
  .dot { width: 7px; height: 7px; border-radius: 50%; flex: none; }
  .dot--cyan { background: var(--accent-cyan); }
  .dot--orange { background: var(--accent-orange); }

  /* Front side */
  .front-brand-panel {
    position: absolute;
    left: 0; top: 0; bottom: 0;
    width: 200px;
    background: linear-gradient(180deg, #121212 0%, #070707 100%);
    border-right: 1px solid var(--card-edge);
  }
  .front-brand {
    position: absolute;
    left: 30px;
    top: 110px;
    display: flex;
    flex-direction: column;
    align-items: flex-start;
    gap: 12px;
  }
  .front-brand .brand-tile { width: 78px; height: 78px; border-radius: 14px; margin-left: 10px; }
  .front-brand .brand-name { font-size: 40px; }
  .contact-block {
    position: absolute;
    left: 234px;
    top: 50px;
    color: var(--text-light);
  }
  .person-name {
    font-family: "Exo 2", Arial, sans-serif;
    font-weight: 700;
    font-size: 27px;
    color: var(--accent-cyan);
    letter-spacing: 0.5px;
    text-transform: uppercase;
  }
  .person-role {
    font-size: 16px;
    color: var(--text-white);
    margin: 2px 0 14px;
  }
  .contact-list { list-style: none; font-size: 12px; line-height: 16px; }
  .contact-list li { display: flex; align-items: flex-start; gap: 10px; margin-bottom: 6px; }
  .contact-list li.gap-above { margin-top: 10px; }
  .icon {
    width: 18px; height: 18px; border-radius: 50%;
    background: var(--accent-orange);
    flex: none;
    display: flex; align-items: center; justify-content: center;
  }
  .icon svg { width: 11px; height: 11px; }
</style>
</head>
<body>

<section class="card card--back" aria-label="Card back">
  <div class="brand-lockup">
    <div class="brand-tile"></div>
    <span class="brand-name">Vorbelt</span>
  </div>
  <ul class="service-list service-list--main">
    <li><span class="dot dot--cyan"></span>Project Management</li>
    <li><span class="dot dot--orange"></span>Consulting</li>
    <li><span class="dot dot--cyan"></span>Master Systems Integrator</li>
  </ul>
  <ul class="service-list service-list--extra">
    <li><span class="dot dot--orange"></span>Datacenter</li>
    <li><span class="dot dot--cyan"></span>Relocations</li>
    <li><span class="dot dot--orange"></span>Restacks</li>
  </ul>
</section>

<section class="card card--front" aria-label="Card front">
  <div class="front-brand-panel">
    <div class="front-brand">
      <div class="brand-tile"></div>
      <span class="brand-name">Vorbelt</span>
    </div>
  </div>
  <div class="contact-block">
    <h1 class="person-name">Marcus Helder</h1>
    <p class="person-role">Director</p>
    <ul class="contact-list">
      <li>
        <span class="icon"><svg viewBox="0 0 12 12"><path d="M6 1a3.5 3.5 0 0 0-3.5 3.5C2.5 7.5 6 11 6 11s3.5-3.5 3.5-6.5A3.5 3.5 0 0 0 6 1z" fill="#1a1a1a"/><circle cx="6" cy="4.5" r="1.3" fill="#f39117"/></svg></span>
        <span>Vorbelt Pte Ltd, 12 Harbour Crest<br>#05-11 Quay Point Tower 2<br>Singapore, 019872</span>
      </li>
      <li class="gap-above">
        <span class="icon"><svg viewBox="0 0 12 12"><path d="M3 1.5l1.6 2.2-1 1.2a6 6 0 0 0 3.5 3.5l1.2-1 2.2 1.6-.8 1.6C6 10.6 1.4 6 1.4 2.3z" fill="#1a1a1a"/></svg></span>
        <span>+65 8476 2153</span>
      </li>
      <li>
        <span class="icon"><svg viewBox="0 0 12 12"><rect x="1.5" y="3" width="9" height="6" fill="#1a1a1a"/><path d="M1.5 3L6 6.5 10.5 3" stroke="#f39117" stroke-width="0.9" fill="none"/></svg></span>
        <span>marcus.helder@vorbelt.com</span>
      </li>
      <li>
        <span class="icon"><svg viewBox="0 0 12 12"><circle cx="6" cy="6" r="4.3" fill="none" stroke="#1a1a1a" stroke-width="1"/><ellipse cx="6" cy="6" rx="1.8" ry="4.3" fill="none" stroke="#1a1a1a" stroke-width="0.9"/><path d="M1.7 6h8.6" stroke="#1a1a1a" stroke-width="0.9"/></svg></span>
        <span>www.vorbelt.com</span>
      </li>
    </ul>
  </div>
</section>

</body>
</html>
```